Bifold brochure design for leadership academy

Please see below. This is a bifold brochure for a leadership academy. (www.vtq.institute). Look and feel must be colours, shapes, abstract designs, graphics, pictures. Make this professional, yet casual and bold.

Feel free to design just the front and back cover, then I'll give feedback on whether or not you're in the right direction.

COVER
- Title: “The Ultimate Gap Year Program”
- “Northbrook Mentorship Institute” logo somewhere
- Subtitles (with images, icons, and/or shapes): “Self-discovery” “Skills development” “Real-world Impact”

PAGE 2 (Inside Fold)
- Title: "The Program"
- Section 2a: Section title: "How it works”
- Image: See website, image under "four phases of the program". Please adapt and make it look better
- Text: NMI is a structured, 8-month ‘gap year’ program for 18-25 year olds who want more than just a year off – they want a year ahead. Our aim is to develop high-potential young leaders with strong values, clear purpose, high-impact skills, and a track record of real-world accomplishments that are second-to-none. We do this through four-phases.
- Section 2b: Section title: “Dates & Timing”
- Image: See image on website under 'dates and timing'. Make sure both dates show up on the brochure (September and January program).
- Text: There are two programs per year: one that starts in September, the other in January. The first four months of the program are based in Toronto at the NMI headquarters. The curriculum we work through is highly engaging and personalized, focusing directly on students’ goals. After that, students are out in the world, achieving the remaining components of the program (e.g. internship, volunteer abroad).

PAGE 3 (Outside Fold)
- Page Title: "The Students"
- Section 3a: Section title: “Who’s it for”
- Subtitle1: “High school graduates”
 Image/icon of a high school grad
 Text1: 90% of high school grads aren't sure why they’re going to university or what they want to study.
 Text2: NMI helps students discover what they truly want to do in life, and make enormous progress towards these goals.

- Subtitle2: “Post-secondary students”
 Image/icon of a university / college student
 Text1: 28% of students switch or drop out of their program because it wasn’t for them or they didn’t like it.
 Text2: Don't keep moving around or risk switching careers down the road – find out what sparks your passion with NMI.

- Subtitle3: “Post-secondary graduates”
 Image/icon of a university/ college grad
 Text1: 50% of graduates are unemployed or underemployed, 60% are in debt.
 Text2: NMI will help you get your dream job – our students won’t settle for anything less.

- Section 3b: Section title: “How to apply”
 Text1: We select high-potential young leaders with a desire to improve themselves and impact the world.
 Text2: We won’t ask you for your grades – we care more about your values and potential.
 Text3: Visit www.vtq.institute to apply now

BACK COVER
- Page Title: “Get in Touch”
- Website: www.vtq.institute
- Facebook page: facebook.com/vtq.institute
- Twitter handle: @vtq_institute
- Email: brent@vtq.institute

Project Deadline Extended Reason: Made a mistake initially only giving designers 2 days to submit. This allows for more high quality designs. Thank you. Added Wednesday, March 18, 2015

18-25 year olds, parents, teachers

Leadership

• Beautiful design - sleek and bold, yet colourful and casual. Keep the colours similar to our website (www.vtq.institute). See examples of other brochures.
• http://img.plorvex.net/jpg/00/11/22/33/240_F_11223344_aBcDeFgHiJkLmNoPqRsTuVwXyZ0123.jpg
• http://quelmarsite.com/wp-content/uploads/2014/11/Sample-Bi-fold-Brochure.jpg
• http://www.vantrello.com/media/k2/galleries/5/001-bi-fold-brochure-psd-mock-up-template.jpg
• http://img.plorvex.net/jpg/00/44/55/66/240_F_44556677_zYxWvUtSrQpOnMlKjIhGfEdCbA9876.jpg

```html
<!DOCTYPE html>
<html lang="en">
<head>
<meta charset="utf-8">
<title>The Students – Northbrook Mentorship Institute</title>
<link rel="stylesheet" href="https://fonts.googleapis.com/css2?family=Open+Sans:wght@400;600;700&display=swap">
<style>
  :root {
    --brand-red: #b01c20;
    --ink: #231f20;
    --paper: #ffffff;
  }
  * { box-sizing: border-box; margin: 0; padding: 0; }
  html, body { width: 1200px; height: 901px; overflow: hidden; background: var(--paper); }
  body { font-family: "Open Sans", Arial, sans-serif; color: var(--ink); }

  .page { position: relative; width: 1200px; height: 901px; overflow: hidden; background: var(--paper); }

  .corner-accent { position: absolute; top: 0; left: 0; width: 1200px; height: 260px; }

  .page-title { position: absolute; left: 46px; top: 38px; }
  .page-title .big {
    display: block; font-weight: 700; font-size: 118px; line-height: 1;
    color: var(--brand-red); letter-spacing: 2px;
  }
  .page-title .sub {
    display: block; font-weight: 700; font-size: 44px; line-height: 1;
    letter-spacing: 10.5px; margin-top: 16px; color: var(--ink);
  }

  .audience { position: absolute; top: 250px; width: 320px; }
  .audience--school { left: 45px; }
  .audience--college { left: 441px; }
  .audience--graduate { left: 838px; }

  .qa { font-weight: 700; font-size: 19px; line-height: 26px; }
  .qa .label { color: var(--brand-red); }

  .portrait { width: 316px; height: 176px; background: var(--brand-red); margin-top: 3px; }
  .audience--graduate .portrait { margin-top: 6px; }

  .facts { list-style: none; margin-top: 12px; font-size: 18.5px; line-height: 25.6px; }
  .facts li::before { content: "• "; }

  .apply-title { position: absolute; left: 46px; top: 728px; }
  .apply-title .big {
    display: block; font-weight: 700; font-size: 132px; line-height: 1;
    color: var(--brand-red); letter-spacing: 1px;
  }
  .apply-title .sub {
    display: block; font-weight: 700; font-size: 38px; line-height: 1;
    letter-spacing: 7px; margin-top: 4px; color: var(--ink);
  }

  .apply-steps {
    position: absolute; left: 438px; top: 745px; width: 720px;
    list-style: none; font-size: 18.5px; line-height: 26px;
  }
  .apply-steps li::before { content: "• "; }
  .apply-steps strong { font-weight: 700; }
</style>
</head>
<body>
<main class="page">
  <svg class="corner-accent" viewBox="0 0 1200 260" aria-hidden="true">
    <polygon points="390,0 1200,0 1200,60 434,207" fill="var(--brand-red)"/>
    <polygon points="434,207 1200,60 1200,85 442,236" fill="var(--ink)"/>
  </svg>

  <h1 class="page-title">
    <span class="big">THE</span>
    <span class="sub">STUDENTS</span>
  </h1>

  <section class="audience audience--school">
    <p class="qa"><span class="label">Q: Who’s it for</span><br><span class="label">A:</span> High school graduates</p>
    <div class="portrait" role="img" aria-label="Illustration of a high school graduate in a varsity jacket"></div>
    <ul class="facts">
      <li>90% of high school grads aren’t sure why they’re going to university or what they want to study.</li>
      <li>NMI helps students discover what they truly want to do in life, and make enormous progress towards these goals.</li>
    </ul>
  </section>

  <section class="audience audience--college">
    <p class="qa"><span class="label">Q: Who’s it for?</span><br><span class="label">A:</span> College students</p>
    <div class="portrait" role="img" aria-label="Illustration of a college student wearing a beret"></div>
    <ul class="facts">
      <li>28% of students switch or drop out of their program because it wasn’t for them or they didn’t like it.</li>
      <li>Don’t keep moving around or risk switching careers down the road – find out what sparks your passion with NMI.</li>
    </ul>
  </section>

  <section class="audience audience--graduate">
    <p class="qa"><span class="label">Q: Who’s it for?</span><br><span class="label">A:</span> Post-secondary graduates</p>
    <div class="portrait" role="img" aria-label="Illustration of a post-secondary graduate in a suit"></div>
    <ul class="facts">
      <li>50% of graduates are unemployed or underemployed, 60% are in debt.</li>
      <li>NMI will help you get your dream job – our students won’t settle for anything less.</li>
    </ul>
  </section>

  <h2 class="apply-title">
    <span class="big">HOW</span>
    <span class="sub">TO APPLY</span>
  </h2>

  <ul class="apply-steps">
    <li>We select high-potential young leaders with a desire to improve themselves and impact the world.</li>
    <li>We won’t ask you for your grades – we care more about your values and potential.</li>
    <li>Visit <strong>www.vtq.institute</strong> to apply now</li>
  </ul>
</main>
</body>
</html>
```